Bright Harbor Dental

Please go to www.brightharbordental-example.com and obtain the current company logo.
Doctors name are
Marisol Ventrada, DDS
Peter Vang, DMD
Addresses are
412 Maple Ridge Rd
Teaneck, NJ 07591
201-555-0147
And
287 52nd St.
West New York, NJ 07058
201-555-0183
Theme of the business card should feel modrrn and similar to the website.
Front side should include company logo, doctors name, addresses, phone numbers.
Back of the card should include blank lines for patient's name. Date and time for next scheduled appointment. And notice of 24-hr cancellation courtesy policy.

```html
<!DOCTYPE html>
<html lang="en">
<head>
<meta charset="UTF-8">
<title>Bright Harbor Dental – Business Cards</title>
<link rel="stylesheet" href="https://fonts.googleapis.com/css2?family=Oswald:wght@500&family=Open+Sans:wght@400&family=Montserrat:wght@400;600;700&display=swap">
<style>
  :root {
    --bg: #e6e6e6;
    --card: #ffffff;
    --ink: #2b2b2b;
    --ink-soft: #4a4a4a;
    --navy: #1f2266;
    --rule: #8a8a8a;
    --dots: #6d6d6d;
  }
  * { box-sizing: border-box; margin: 0; padding: 0; }
  html, body { width: 1200px; height: 1000px; overflow: hidden; }
  body {
    background: var(--bg);
    display: flex;
    flex-direction: column;
    align-items: center;
    justify-content: center;
    gap: 26px;
  }
  .card {
    width: 820px;
    height: 460px;
    background: var(--card);
    border-radius: 24px;
    box-shadow: 0 6px 20px rgba(0,0,0,0.12);
    position: relative;
    font-family: 'Montserrat', sans-serif;
    color: var(--ink);
  }
  .brand {
    display: flex;
    align-items: center;
    justify-content: center;
    gap: 14px;
  }
  .brand-dot {
    width: 26px; height: 26px;
    border-radius: 50%;
    background: var(--navy);
  }
  .brand-name {
    font-family: 'Montserrat', sans-serif;
    font-weight: 700;
    font-size: 40px;
    letter-spacing: 1px;
    color: var(--ink);
  }

  /* Appointment side */
  .appointment { padding: 48px 70px 0; }
  .appointment .brand { margin-bottom: 44px; }
  .appointment-title {
    font-weight: 700;
    font-size: 18px;
    letter-spacing: 0.5px;
    color: var(--navy);
    margin-bottom: 20px;
  }
  .field-row {
    display: flex;
    align-items: flex-end;
    gap: 10px;
    font-size: 18px;
    color: var(--ink-soft);
    letter-spacing: 0.5px;
    margin-bottom: 26px;
  }
  .fill {
    flex: 1;
    border-bottom: 2px dotted var(--dots);
    height: 18px;
  }
  .policy {
    text-align: center;
    font-weight: 600;
    font-size: 18px;
    letter-spacing: 2px;
    margin-top: 22px;
  }

  /* Contact side */
  .contact { padding: 56px 60px 0; }
  .contact .brand { margin-bottom: 50px; }
  .doctors {
    display: flex;
    justify-content: center;
    align-items: stretch;
  }
  .doctor { width: 320px; }
  .doctor.left { text-align: right; padding-right: 22px; }
  .doctor.right { text-align: left; padding-left: 22px; padding-top: 8px; }
  .divider { width: 3px; background: var(--rule); }
  .doctor-name {
    font-family: 'Oswald', sans-serif;
    font-weight: 500;
    font-size: 30px;
    letter-spacing: 1.5px;
    text-transform: uppercase;
    margin-bottom: 8px;
  }
  .doctor-line {
    font-family: 'Open Sans', sans-serif;
    font-size: 20px;
    line-height: 1.35;
    color: var(--ink-soft);
  }
  .phone {
    display: inline-flex;
    align-items: center;
    gap: 10px;
  }
  .phone svg { width: 16px; height: 16px; fill: var(--navy); }
  .website {
    font-family: 'Open Sans', sans-serif;
    font-size: 21px;
    color: var(--ink-soft);
    text-align: center;
    margin-top: 42px;
    letter-spacing: 0.5px;
  }
</style>
</head>
<body>

  <section class="card appointment">
    <div class="brand">
      <span class="brand-dot"></span>
      <span class="brand-name">BRIGHT HARBOR DENTAL</span>
    </div>
    <h2 class="appointment-title">YOUR NEXT APPOINTMENT</h2>
    <div class="field-row"><span>Patient's Name:</span><span class="fill"></span></div>
    <div class="field-row">
      <span>date:</span><span class="fill"></span>
      <span>time:</span><span class="fill"></span>
      <span>day:</span><span class="fill"></span>
    </div>
    <p class="policy">24-HR CANCELLATION COURTESY POLICY</p>
  </section>

  <section class="card contact">
    <div class="brand">
      <span class="brand-dot"></span>
      <span class="brand-name">BRIGHT HARBOR DENTAL</span>
    </div>
    <div class="doctors">
      <div class="doctor left">
        <h3 class="doctor-name">Marisol Ventrada, DDS</h3>
        <p class="doctor-line">412 Maple Ridge Rd</p>
        <p class="doctor-line">Teaneck, NJ 07591</p>
        <p class="doctor-line phone">201 555 0147
          <svg viewBox="0 0 24 24" aria-hidden="true"><path d="M6.6 10.8a15.1 15.1 0 0 0 6.6 6.6l2.2-2.2a1 1 0 0 1 1-.25 11.4 11.4 0 0 0 3.6.57 1 1 0 0 1 1 1V20a1 1 0 0 1-1 1A17 17 0 0 1 3 4a1 1 0 0 1 1-1h3.5a1 1 0 0 1 1 1c0 1.25.2 2.45.57 3.57a1 1 0 0 1-.25 1z"/></svg>
        </p>
      </div>
      <div class="divider"></div>
      <div class="doctor right">
        <h3 class="doctor-name">Peter Vang, DMD</h3>
        <p class="doctor-line">287 52nd St.</p>
        <p class="doctor-line">West New York, NJ 07058</p>
        <p class="doctor-line phone">
          <svg viewBox="0 0 24 24" aria-hidden="true"><path d="M6.6 10.8a15.1 15.1 0 0 0 6.6 6.6l2.2-2.2a1 1 0 0 1 1-.25 11.4 11.4 0 0 0 3.6.57 1 1 0 0 1 1 1V20a1 1 0 0 1-1 1A17 17 0 0 1 3 4a1 1 0 0 1 1-1h3.5a1 1 0 0 1 1 1c0 1.25.2 2.45.57 3.57a1 1 0 0 1-.25 1z"/></svg>
          201 555 0183</p>
      </div>
    </div>
    <p class="website">www.brightharbordental-example.com</p>
  </section>

</body>
</html>
```